Wine Bottle Lable

Want a unique, simple but elegant, label for a wine bottle. I want to use the letters "DKP" in the design which is a moniker for my last name "Dufkamp". The letters DKP do not have to be juxtaposed together so that it is recognizable, or they could be something like D-KP, KP-D, DPK D-KP-D, etc. The X could be totally separated from the NO, or otherwise. The wine is a white wine in a clear bottle. I need Adobe Illustrator files so I can add the wine varietal, year, alcohol content. The label should be 4" wide and 5" tall.

Colors

Designer to choose colors to be used in the design.

Requirements
Nice to have
• outstanding but simple graphics

```html
<!DOCTYPE html>
<html lang="en">
<head>
<meta charset="utf-8">
<title>DPK Chardonnay Label</title>
<link rel="stylesheet" href="https://fonts.googleapis.com/css2?family=Tinos:wght@400;700&family=Great+Vibes&family=Arimo:wght@400&display=swap">
<style>
  :root {
    --backdrop: #dfe5e6;
    --label-black: #0b0d0c;
    --wave-green: #1d4a2c;
    --gold: #e2b23a;
    --gold-soft: #f2c74a;
    --white: #f4f4f2;
  }
  * { margin: 0; padding: 0; box-sizing: border-box; }
  html, body {
    width: 1182px;
    height: 1200px;
    overflow: hidden;
    background: var(--backdrop);
  }
  .label {
    position: absolute;
    left: 156px;
    top: 100px;
    width: 870px;
    height: 1000px;
    background: var(--label-black);
    overflow: hidden;
  }
  .label__pattern {
    position: absolute;
    inset: 0;
    width: 100%;
    height: 100%;
  }
  .label__content {
    position: absolute;
    inset: 0;
    text-align: center;
    color: var(--white);
  }
  .brand {
    position: absolute;
    top: 70px;
    left: 0;
    right: 0;
    font-family: "Tinos", serif;
    font-weight: 400;
    font-size: 200px;
    line-height: 1;
    letter-spacing: 6px;
    color: var(--gold);
  }
  .vintage {
    position: absolute;
    top: 450px;
    left: 0;
    right: 0;
    font-family: "Tinos", serif;
    font-size: 72px;
    line-height: 1;
  }
  .varietal {
    position: absolute;
    top: 525px;
    left: 0;
    right: 0;
    font-family: "Great Vibes", cursive;
    font-size: 120px;
    line-height: 1;
  }
  .reserve {
    position: absolute;
    top: 705px;
    left: 0;
    right: 0;
    font-family: "Tinos", serif;
    font-size: 46px;
    line-height: 1.15;
    color: var(--gold-soft);
  }
  .detail {
    position: absolute;
    bottom: 40px;
    font-family: "Arimo", sans-serif;
    font-size: 38px;
    line-height: 1;
    color: var(--white);
  }
  .detail--volume { left: 32px; font-size: 44px; }
  .detail--alcohol { right: 36px; }
</style>
</head>
<body>
  <main class="label">
    <svg class="label__pattern" viewBox="0 0 870 1000" role="img" aria-label="Decorative pattern of broad green concentric waves on black" preserveAspectRatio="none">
      <defs>
        <radialGradient id="wave-tone" cx="50%" cy="45%" r="70%">
          <stop offset="0%" stop-color="#143321"/>
          <stop offset="100%" stop-color="#0b0d0c"/>
        </radialGradient>
      </defs>
      <rect width="870" height="1000" fill="url(#wave-tone)"/>
    </svg>
    <div class="label__content">
      <h1 class="brand">DPK</h1>
      <p class="vintage">2012</p>
      <p class="varietal">Chardonnay</p>
      <p class="reserve">Reserve<br>Wine Valley Vineyard</p>
      <p class="detail detail--volume">750ml</p>
      <p class="detail detail--alcohol">Alc. 14% by Vol.</p>
    </div>
  </main>
</body>
</html>
```